Tumbleweed Backpackers DL Flyer Design

We require a two sided Flyer design to help promote Tumbleweed's Backpackers / Hostel accommodation.Give it a warm, summer vibe  to reflect Perth's great weather and the friendly hospitality that Tumbleweed's provides. Please use the attached pictures, logo and text. Our colour scheme is usually pastel blues but some warm accent colours could work too.
General advice:
The front should be exciting with pictures (or photos) that draw people in, with our contact info at the bottom.
The back should contain our bullet points, the location map with Tumbleweed address and photos.
It needs to appeal to 18 - 29 yr olds as this is our target market.
Size: 100 x 210 mm
Address: 87 Marrowvale Rd, East Perth, Western Australia, 6000, Australia
Website: http://www.tumbleweedbackpackers.com.au/
Email: reservations@tumbleweedbackpackers.com.au
Ph: +61 8 9471 3062

Target Market(s)
18 - 29
Industry/Entity Type
Accommodation

```html
<!DOCTYPE html>
<html lang="en">
<head>
<meta charset="utf-8">
<title>Tumbleweed Backpackers – DL Flyer</title>
<link rel="stylesheet" href="https://fonts.googleapis.com/css2?family=Lato:ital,wght@0,400;0,700;0,900;1,400&family=Sniglet:wght@400;800&display=swap">
<style>
  :root {
    --page-bg: #d8d3cc;
    --paper: #ffffff;
    --paper-shade: #e9eaec;
    --navy: #0d2f72;
    --royal: #1f5cb4;
    --sky: #34a3e2;
    --ink: #1c1c1c;
    --muted-ink: #333333;
    --accent-blue: #1e8fd6;
    --white: #ffffff;
  }
  * { box-sizing: border-box; margin: 0; padding: 0; }
  html, body { width: 708px; height: 1200px; overflow: hidden; }
  body { background: var(--page-bg); position: relative; font-family: "Lato", sans-serif; }

  .flyer {
    position: absolute; left: 88px; top: 28px;
    width: 544px; height: 1147px;
    background: linear-gradient(180deg, var(--paper) 0%, var(--paper-shade) 100%);
    overflow: hidden;
  }
  .hero-photo {
    position: absolute; left: 0; top: 130px; width: 544px; height: 400px;
    background: linear-gradient(160deg, #cfc6bb 0%, #8d7f70 45%, #4a4038 100%);
  }
  .flyer-shapes { position: absolute; inset: 0; }

  .brand { position: absolute; left: 90px; top: 14px; display: flex; align-items: center; gap: 22px; }
  .brand-mark { width: 112px; height: 112px; border-radius: 50%; background: var(--royal); }
  .brand-name { font-weight: 900; font-size: 34px; line-height: 38px; color: var(--ink); }

  .section-title {
    position: absolute; left: 0; right: 0; top: 552px;
    text-align: center; font-family: "Sniglet", sans-serif; font-weight: 400;
    font-size: 44px; color: var(--white); letter-spacing: 0.5px;
  }

  .features {
    position: absolute; list-style: none;
    font-style: italic; font-size: 16px; line-height: 21px; color: var(--white);
  }
  .features li { position: relative; padding-left: 16px; margin-bottom: 8px; white-space: nowrap; }
  .features li::before {
    content: ""; position: absolute; left: -2px; top: 7px;
    width: 7px; height: 7px; border-radius: 50%; background: var(--sky);
  }
  .features-left { left: 60px; top: 626px; width: 220px; }
  .features-right { left: 325px; top: 623px; width: 200px; }

  .contact { position: absolute; top: 1046px; left: 0; right: 0; height: 100px; }
  .address { position: absolute; left: 27px; top: 2px; font-size: 14px; line-height: 18.5px; color: var(--muted-ink); font-style: normal; }
  .contact-label { position: absolute; font-family: "Sniglet", sans-serif; font-size: 17px; color: var(--accent-blue); left: 180px; }
  .contact-label.call { top: 0; }
  .contact-label.visit { top: 40px; }
  .contact-value { position: absolute; left: 180px; font-size: 14px; color: var(--ink); }
  .contact-value.phone { top: 20px; font-weight: 700; }
  .contact-value.web { top: 58px; }

  .cook-photo {
    position: absolute; left: 432px; top: 982px; width: 90px; height: 165px;
    border-radius: 40px 40px 6px 6px;
    background: linear-gradient(180deg, #6a5a50 0%, #2a2a2e 55%, #1a1a1c 100%);
  }
</style>
</head>
<body>
  <main class="flyer">
    <div class="hero-photo" role="img" aria-label="Photo of four smiling backpackers sharing breakfast at a hostel kitchen table"></div>

    <svg class="flyer-shapes" width="544" height="1147" viewBox="0 0 544 1147" aria-hidden="true">
      <defs>
        <linearGradient id="panelFill" x1="0" y1="0" x2="0" y2="1">
          <stop offset="0" stop-color="#2c69c0"/>
          <stop offset="0.5" stop-color="#1a4a9a"/>
          <stop offset="1" stop-color="#0b2a66"/>
        </linearGradient>
        <linearGradient id="headerFill" x1="0" y1="0" x2="0" y2="1">
          <stop offset="0" stop-color="#ffffff"/>
          <stop offset="1" stop-color="#eeeff1"/>
        </linearGradient>
      </defs>
      <path d="M0,0 H544 V160 Q272,100 0,190 Z" fill="url(#headerFill)"/>
      <path d="M0,196 Q272,106 544,166" fill="none" stroke="#0d3f94" stroke-width="14"/>
      <path d="M0,210 Q272,120 544,180" fill="none" stroke="var(--sky)" stroke-width="6"/>
      <path d="M0,220 Q272,130 544,190" fill="none" stroke="#ffffff" stroke-width="6"/>
      <path d="M0,470 Q272,550 544,465 V1147 H0 Z" fill="url(#panelFill)"/>
      <path d="M0,452 Q272,532 544,447" fill="none" stroke="#ffffff" stroke-width="8"/>
      <path d="M0,462 Q272,542 544,457" fill="none" stroke="var(--sky)" stroke-width="10"/>
      <path d="M0,980 Q272,1040 544,955" fill="none" stroke="#111111" stroke-width="6"/>
      <path d="M0,990 Q272,1050 544,965 V1147 H0 Z" fill="url(#headerFill)"/>
    </svg>

    <header class="brand">
      <span class="brand-mark"></span>
      <span class="brand-name">Tumbleweed's<br>Backpackers</span>
    </header>

    <h2 class="section-title">why choose us</h2>

    <ul class="features features-left">
      <li>Huge games, Movies<br>and TV areas</li>
      <li>Basket Ball, Table Tennis,<br>Pool tableand much more!</li>
      <li>Free Computer use</li>
      <li>Food and drinks available<br>licensed bar</li>
      <li>Free bus and easy<br>access to transport</li>
      <li>Close to local and<br>interstate trains</li>
      <li>Walking distance to<br>nightlife areas Safe<br>secure parking</li>
    </ul>

    <ul class="features features-right">
      <li>Award Winning</li>
      <li>Ensuite Dorm rooms</li>
      <li>Private lockers<br>for every person</li>
      <li>Female only<br>dorms available</li>
      <li>Free breakfast<br>and linen</li>
      <li>Free wifi</li>
      <li>Excellent kitchen<br>and dining facilities</li>
      <li>Laundry facilities<br>on site</li>
      <li>24hr reception</li>
    </ul>

    <div class="cook-photo" role="img" aria-label="Photo of a smiling hostel guest holding a frying pan and spatula"></div>

    <footer class="contact">
      <address class="address">87 Marrowvale Rd,<br>East Perth,<br>Western Australia,<br>6000, Australia</address>
      <span class="contact-label call">Call</span>
      <span class="contact-value phone">61 8 9471 3062</span>
      <span class="contact-label visit">Visit us</span>
      <span class="contact-value web">www.tumbleweedbackpackers.com.au</span>
    </footer>
  </main>
</body>
</html>
```